Brochure for medical doctor

I need a brochure for a medical doctor to promote his practice. The brochure should contain his picture, business information (use letterhead from attachment), and the following text:

- Now accepting PI cases on lien!
- Same and next business day appointments available for initial visits, pre-operative clearances, and all other medical needs

- Expedited medical reports sent quickly to your office

Medical

```html
<!DOCTYPE html>
<html lang="en">
<head>
<meta charset="utf-8">
<title>Lakeside Medical Center – Brochure</title>
<link href="https://fonts.googleapis.com/css2?family=Open+Sans:wght@300;400;600;700;800&display=swap" rel="stylesheet">
<style>
  :root {
    --green-deep: #0b4f2b;
    --green-band-top: #1b7a3c;
    --green-band-bottom: #0e9a4a;
    --grey-light: #e2e3e3;
    --ink: #1f1f1f;
    --accent-yellow: #f1f7a1;
    --white: #ffffff;
  }
  * { margin: 0; padding: 0; box-sizing: border-box; }
  html, body { width: 849px; height: 1200px; overflow: hidden; background: var(--white); }
  body { font-family: "Open Sans", Arial, sans-serif; }

  .brochure { position: relative; width: 849px; height: 1200px; overflow: hidden; background: var(--white); }

  .health-band {
    position: absolute; left: 0; top: 347px; width: 849px; height: 431px;
    background: linear-gradient(180deg, var(--green-band-top), var(--green-band-bottom));
  }
  .title-disc {
    position: absolute; left: -78px; top: -205px; width: 566px; height: 566px;
    border-radius: 50%; background: var(--grey-light);
  }
  .practice-name {
    position: absolute; left: 56px; top: 92px;
    font-weight: 700; font-size: 46px; line-height: 58px;
    color: var(--green-deep);
  }

  .icon-disc {
    position: absolute; left: 510px; top: 199px; width: 268px; height: 268px;
    border-radius: 50%; background: var(--white);
    display: flex; align-items: center; justify-content: center;
  }
  .icon-disc .inner {
    width: 244px; height: 244px; border-radius: 50%; background: var(--grey-light);
    display: flex; align-items: center; justify-content: center;
  }
  .icon-disc .stethoscope-area {
    width: 140px; height: 140px; border-radius: 30px;
    background: radial-gradient(circle, #9a9a9a 0%, #d6d6d6 75%);
  }

  .tagline { position: absolute; left: 48px; top: 440px; color: var(--white); }
  .tagline .lead { font-weight: 300; font-size: 51px; line-height: 60px; letter-spacing: 0.5px; }
  .tagline .emphasis { font-weight: 800; font-size: 62px; line-height: 72px; color: var(--accent-yellow); letter-spacing: 1px; }

  .portrait-ring {
    position: absolute; left: 49px; top: 651px; width: 368px; height: 368px;
    border-radius: 50%; background: var(--white);
    display: flex; align-items: center; justify-content: center;
  }
  .portrait {
    width: 344px; height: 344px; border-radius: 50%; background: var(--green-deep);
    display: flex; flex-direction: column; align-items: center; padding-top: 100px;
    color: var(--white); text-align: center;
  }
  .portrait .placeholder-mark { width: 114px; height: 92px; border: 9px solid var(--white); border-radius: 18px; margin-bottom: 18px; }
  .portrait .placeholder-text { font-size: 21px; line-height: 30px; font-weight: 400; }

  .doctor-card {
    position: absolute; left: 35px; top: 969px; width: 394px; height: 102px;
    border-radius: 28px; background: var(--grey-light); text-align: center; padding-top: 16px;
  }
  .doctor-card .name { font-weight: 700; font-size: 29px; line-height: 38px; color: var(--ink); }
  .doctor-card .credentials { font-size: 17px; line-height: 26px; color: var(--ink); }

  .services-card {
    position: absolute; left: 442px; top: 612px; width: 380px; height: 467px;
    border-radius: 38px; background: var(--white); padding: 8px;
  }
  .services-card .panel {
    width: 100%; height: 100%; border-radius: 30px; background: var(--grey-light);
    text-align: center; color: var(--ink); font-weight: 600; font-size: 18px; line-height: 35px;
    padding: 52px 10px 0;
  }
  .services-card .first { margin-bottom: 56px; }
  .services-card .second { margin-bottom: 54px; }

  .contact-bar {
    position: absolute; left: 0; top: 1114px; width: 849px; height: 76px;
    background: var(--green-deep); color: var(--white);
    display: flex; align-items: center; padding-left: 38px;
    font-weight: 700; font-size: 17px;
  }
  .contact-bar .pin { margin-right: 18px; }
  .contact-bar .address { margin-right: 38px; }
</style>
</head>
<body>
<main class="brochure">
  <div class="health-band"></div>
  <div class="title-disc"></div>

  <h1 class="practice-name">LAKESIDE<br>MEDICAL CENTER</h1>

  <div class="icon-disc">
    <div class="inner">
      <div class="stethoscope-area" role="img" aria-label="Stethoscope icon"></div>
    </div>
  </div>

  <div class="tagline">
    <div class="lead">YOUR HEALTH</div>
    <div class="emphasis">MATTERS</div>
  </div>

  <div class="portrait-ring">
    <div class="portrait" role="img" aria-label="Portrait photo of the doctor">
      <div class="placeholder-mark"></div>
      <div class="placeholder-text">YOUR IMAGE<br>GOES HERE</div>
    </div>
  </div>

  <div class="doctor-card">
    <div class="name">DR. JHON DOE</div>
    <div class="credentials">MD - HU, Prof</div>
  </div>

  <section class="services-card">
    <div class="panel">
      <p class="first">Now accepting PI cases on lien!</p>
      <p class="second">Same and next business day<br>appointments available for initial<br>visits, pre-operative clearances,<br>and all other medical needs</p>
      <p>Expedited medical reports sent<br>quickly to your office</p>
    </div>
  </section>

  <footer class="contact-bar">
    <svg class="pin" width="42" height="42" viewBox="0 0 42 42" aria-hidden="true">
      <circle cx="21" cy="21" r="19" fill="none" stroke="var(--white)" stroke-width="2.5"/>
      <path d="M21 9a8 8 0 0 0-8 8c0 6 8 15 8 15s8-9 8-15a8 8 0 0 0-8-8z" fill="var(--white)"/>
      <circle cx="21" cy="17" r="3" fill="var(--green-deep)"/>
    </svg>
    <span class="address">4150 Linden Ave. Oak Hollow, CA, 90000</span>
    <span class="phones">(555) 014-2200&nbsp;&nbsp;Fax (555) 014-2201</span>
  </footer>
</main>
</body>
</html>
```